Larkin Ridge Provisions Co Website Creation

We need a website designed that goes along with our western/cattle brand vibe that our logo has. We are going to need a couple different pages including: About Us, Meat Boxes, Recipes, Contact Us.

We are going to need a shop so that people may visit the website and order meat boxes to be shipped or delivered at their home. Our mission is to provide the highest quality meat that every family can afford.

Would love to see the website design with lots of mountain range backgrounds and create a feel of open range beef that has a tradition of providing great beef. Family owned business that has been raising cattle for over 30 years.

Love the colors of using dark greens, browns, Tans, Blacks

```html
<!DOCTYPE html>
<html lang="en">
<head>
<meta charset="utf-8">
<title>Larkin Ridge Provisions Co</title>
<link href="https://fonts.googleapis.com/css2?family=Oswald:wght@500;600;700&family=Poppins:wght@400;500;600;700&family=Lato:wght@400;700&display=swap" rel="stylesheet">
<style>
:root{
  --green-dark:#0b3a0b;
  --green:#124d12;
  --green-deep:#072607;
  --maroon:#3c0b08;
  --maroon-deep:#1f0504;
  --text:#2b2b2b;
  --muted:#8a8a8a;
  --star:#f2a516;
  --white:#fff;
  --line:#dcdcdc;
}
*{box-sizing:border-box;margin:0;padding:0}
html,body{width:1200px;height:3925px;overflow:hidden;background:#fff}
body{font-family:'Poppins',sans-serif;color:var(--text)}
.page{position:relative;width:1200px;height:3925px;overflow:hidden}
.abs{position:absolute}
.display{font-family:'Oswald',sans-serif;font-weight:700;letter-spacing:1px;text-transform:uppercase}

.topbar{left:0;top:0;width:1200px;height:52px;background:var(--green-dark);color:#fff;display:flex;justify-content:center;align-items:center;gap:18px;font-family:'Oswald',sans-serif;font-size:11px;letter-spacing:.8px}
.header{left:0;top:52px;width:1200px;height:128px;background:#fff;border-bottom:1px solid #eee}
.logo{left:110px;top:66px;width:150px;color:var(--green);font-family:'Oswald',sans-serif;font-weight:700;font-size:21px;line-height:25px;text-transform:uppercase;text-align:center}
.search{left:368px;top:69px;width:720px;height:41px;border:1px solid #cfcfcf;display:flex}
.search span{flex:1;padding:0 18px;line-height:39px;font-size:14px;color:#999}
.search i{width:45px;height:39px;background:var(--green-dark);display:flex;align-items:center;justify-content:center}
.nav{left:368px;top:128px;width:720px;height:52px;border-top:1px solid #eee}
.nav a{position:absolute;top:18px;font-family:'Oswald',sans-serif;font-weight:500;font-size:13px;letter-spacing:.5px;color:#111;text-decoration:none}
.nav a.active{color:var(--green)}
.nav a.active::before{content:"";position:absolute;left:-2px;top:-19px;width:38px;height:3px;background:var(--green)}

.hero{left:0;top:180px;width:1200px;height:510px;background:linear-gradient(180deg,#6f7b4a 0%,#8a9a52 30%,#6d8036 60%,#7f8c45 100%)}
.hero .shade{position:absolute;inset:0;background:linear-gradient(90deg,rgba(40,45,20,.55),rgba(40,45,20,0) 60%)}
.hero-copy{left:111px;top:258px;color:#fff}
.hero-copy .eyebrow{font-family:'Oswald',sans-serif;font-size:14px;letter-spacing:4px}
.hero-copy h1{font-family:'Oswald',sans-serif;font-weight:700;font-size:50px;line-height:62px;margin-top:6px;letter-spacing:1px}
.hero-copy h2{font-weight:600;font-size:16px;margin-top:2px}
.hero-copy p{font-size:13.5px;line-height:26px;width:440px;margin-top:10px;font-weight:500}
.btn-pill{display:inline-block;background:#fff;color:var(--green);border-radius:24px;font-family:'Oswald',sans-serif;font-weight:600;font-size:14px;letter-spacing:1px}
.hero .btn-pill{position:absolute;left:111px;top:500px;width:128px;height:45px;line-height:45px;text-align:center}
.dots{left:111px;top:598px;display:flex;gap:8px}
.dots b{width:8px;height:8px;border-radius:50%;background:rgba(255,255,255,.45)}
.dots b:first-child{background:#fff}

.promo-main{left:111px;top:763px;width:305px;height:471px;background:linear-gradient(135deg,var(--maroon) 0%,#2a0605 45%,#4a100b 55%,var(--maroon-deep) 100%);color:#fff;text-align:center}
.promo-main h3{font-family:'Oswald',sans-serif;font-size:40px;margin-top:46px;letter-spacing:1px}
.promo-main em{display:block;font-size:20px;margin-top:10px}
.promo-main strong{display:block;font-size:40px;margin-top:10px;font-weight:600}
.promo-main p{font-size:14px;line-height:29px;width:260px;margin:14px auto 0}
.promo-main .ghost{display:inline-block;margin-top:28px;width:136px;height:46px;line-height:42px;border:2px solid #fff;border-radius:24px;font-family:'Oswald',sans-serif;font-size:13px;letter-spacing:1px}
.tile{color:#fff;font-family:'Oswald',sans-serif;font-weight:500;font-size:13px;letter-spacing:.8px;line-height:26px}
.tile-meat{left:439px;top:762px;width:649px;height:224px;background:radial-gradient(ellipse at 50% 80%,#7a1d18 0%,#3a1a14 45%,#1c120e 100%)}
.tile-meat span{position:absolute;top:20px;left:0;width:100%;text-align:center;font-size:15px}
.tile-a{left:439px;top:1010px;width:312px;height:224px;background:linear-gradient(160deg,#5d7a8a 0%,#8fa57a 40%,#4f7a2e 75%,#3b6120 100%)}
.tile-b{left:774px;top:1010px;width:314px;height:224px;background:linear-gradient(180deg,#34504a 0%,#a87a50 40%,#557a2a 65%,#2f5b18 100%)}
.tile-a span{position:absolute;left:16px;top:14px}
.tile-b span{position:absolute;left:13px;top:78px;font-size:14px;line-height:29px}

.sec-title{left:0;width:1200px;text-align:center;color:var(--green-deep);font-family:'Oswald',sans-serif;font-weight:700;font-size:42px;letter-spacing:1.5px}
.arrow{width:22px;height:22px;border-radius:50%;display:flex;align-items:center;justify-content:center}
.card{width:224px;height:368px;top:1406px}
.card .img{position:absolute;left:0;top:0;width:224px;height:231px;background:#fff;box-shadow:0 2px 8px rgba(0,0,0,.12)}
.card .img div{position:absolute;inset:40px 30px 40px 30px;border-radius:14px}
.card .tag{position:absolute;left:21px;top:18px;background:var(--green-deep);color:#fff;font-size:11px;font-weight:500;padding:6px 11px}
.card .name{position:absolute;left:10px;top:244px;width:210px;font-size:12.5px;line-height:26px;color:#555;text-transform:uppercase}
.card .stars{position:absolute;left:10px;top:302px;color:var(--star);font-size:12px;letter-spacing:1px}
.card .price{position:absolute;left:10px;top:326px;font-size:20px;font-weight:700;color:var(--maroon)}
.card.featured{border:1px solid #8a8a8a;box-shadow:0 3px 10px rgba(0,0,0,.2);background:#fff}
.card.featured .img{left:8px;top:8px;width:206px;height:217px;box-shadow:none;background:linear-gradient(150deg,#9a1c22 0%,#5c1014 35%,#c4313a 55%,#2a2a2e 100%)}
.card.featured .name{color:#111}
.card.featured .price{color:var(--green)}

.about-bg{left:0;top:1830px;width:1200px;height:440px;background:linear-gradient(180deg,#fff 0%,#fff 55%,#e7eef7 100%)}
.about-copy{left:170px;top:1950px;width:860px;text-align:center;color:var(--green-deep);font-family:'Lato',sans-serif;font-size:14.5px;line-height:26px}
.about-copy p+p{margin-top:47px}
.btn-green{left:536px;top:2184px;width:128px;height:46px;border-radius:24px;background:var(--green-dark);color:#fff;text-align:center;line-height:46px;font-family:'Oswald',sans-serif;font-weight:600;font-size:15px;letter-spacing:1px;box-shadow:0 3px 6px rgba(0,0,0,.25)}
.range{left:0;top:2254px;width:1200px;height:562px;background:linear-gradient(180deg,#e7eef7 0%,#a9bdd8 22%,#8ea3c4 45%,#9d8e7a 62%,#b08a55 75%,#8d6a3a 100%)}

.review{background:#fff;border:1px solid #dcdcdc;box-shadow:0 2px 10px rgba(0,0,0,.06)}
.review .stars{position:absolute;left:22px;top:24px;color:var(--star);font-size:20px;letter-spacing:1px}
.review p{position:absolute;left:22px;top:68px;width:270px;font-size:15.5px;line-height:27.5px;color:#333}
.review .who{position:absolute;left:22px;display:flex;align-items:center;gap:12px}
.review .avatar{width:64px;height:64px;border-radius:50%;background:linear-gradient(180deg,#c9c9c9,#6f7a85)}
.review .who b{display:block;font-size:16px;color:#111}
.review .who small{font-size:14px;color:#999}
.review.plain{border:none;box-shadow:0 4px 14px rgba(0,0,0,.08)}

.subscribe{left:111px;top:3460px;width:977px;height:96px;border-radius:48px;background:var(--green-deep);z-index:2}
.subscribe h4{position:absolute;left:87px;top:31px;color:#fff;font-family:'Oswald',sans-serif;font-size:24px;letter-spacing:2px;font-weight:600}
.subscribe .field{position:absolute;left:453px;top:25px;width:440px;height:46px;border-radius:24px;background:#fff}
.subscribe .field span{position:absolute;left:22px;top:15px;font-size:12px;color:#777}
.subscribe .field b{position:absolute;right:5px;top:5px;width:122px;height:36px;border-radius:18px;background:var(--maroon);color:#fff;text-align:center;line-height:36px;font-family:'Oswald',sans-serif;font-size:12px;letter-spacing:1px;font-weight:500}
.footer{left:0;top:3520px;width:1200px;height:405px;background:var(--green-dark);color:#fff}
.fcol{position:absolute;top:109px}
.fcol h5{font-family:'Oswald',sans-serif;font-weight:600;font-size:16px;letter-spacing:2px}
.fcol ul{list-style:none;margin-top:20px}
.fcol li{font-size:14px;line-height:27.5px;color:#e0e8e0}
.fcontact li{display:flex;gap:10px;align-items:flex-start;line-height:20px;margin-bottom:14px}
.fbrand{position:absolute;left:870px;top:94px;width:218px;text-align:center;font-family:'Oswald',sans-serif;font-weight:700;font-size:30px;line-height:38px;text-transform:uppercase}
.copyright{position:absolute;left:111px;top:327px;width:977px;display:flex;align-items:center;gap:14px;font-size:11px}
.copyright i{flex:1;height:1px;background:#b8c8b8}
</style>
</head>
<body>
<div class="page">

  <div class="abs topbar"><span>UP TO 75% OFF WEEKEND MEGA DEALS</span><span>|</span><span>SHOP NOW</span></div>

  <header class="abs header"></header>
  <div class="abs logo">Larkin Ridge<br>Provisions Co</div>
  <div class="abs search"><span>Search...</span><i><svg width="14" height="14" viewBox="0 0 14 14"><circle cx="6" cy="6" r="4" stroke="#fff" stroke-width="2" fill="none"/><path d="M9 9l3.5 3.5" stroke="#fff" stroke-width="2"/></svg></i></div>
  <nav class="abs nav">
    <a class="active" style="left:4px">HOME</a>
    <a style="left:119px">ABOUT</a>
    <a style="left:229px">MEAT BOXES</a>
    <a style="left:369px">RECIPES</a>
    <a style="left:499px">CONTACT US</a>
    <svg class="abs" style="left:602px;top:18px" width="18" height="18" viewBox="0 0 18 18"><circle cx="9" cy="5" r="4" fill="#111"/><path d="M1 18c0-5 4-7 8-7s8 2 8 7z" fill="#111"/></svg>
    <svg class="abs" style="left:649px;top:14px" width="24" height="22" viewBox="0 0 24 22"><path d="M1 6h4l3 10h11l3-8H7" stroke="#111" stroke-width="2" fill="none"/><circle cx="10" cy="19" r="2" fill="#111"/><circle cx="17" cy="19" r="2" fill="#111"/><circle cx="19" cy="5" r="5" fill="var(--green)"/><text x="19" y="8" font-size="7" fill="#fff" text-anchor="middle" font-family="Poppins">0</text></svg>
    <svg class="abs" style="left:703px;top:20px" width="17" height="15" viewBox="0 0 17 15"><path d="M8.5 15L1.5 8A4 4 0 018.5 2.5 4 4 0 0115.5 8z" fill="#111"/></svg>
  </nav>

  <section class="abs hero" role="img" aria-label="Herd of dark cattle grazing on a green open range in front of rolling hills">
    <div class="shade"></div>
  </section>
  <div class="abs hero-copy">
    <div class="eyebrow">WELCOME TO</div>
    <h1>LARKIN RIDGE PROVISIONS CO</h1>
    <h2>WE ARE A FAMILY-OWNED BUSINESS</h2>
    <p>Itaque earum rerum hic tenetur a sapiente delectus, ut aut reiciendis voluptatibus maiores alias consequatur aut perferendis doloribus asperiores repellat.</p>
  </div>
  <a class="btn-pill" style="position:absolute;left:111px;top:500px;width:128px;height:45px;line-height:45px;text-align:center;box-shadow:0 2px 6px rgba(0,0,0,.25)">SHOP NOW</a>
  <div class="abs dots"><b></b><b></b><b></b><b></b></div>

  <div class="abs promo-main">
    <h3>FRESH MEAT</h3>
    <em>Get Upto</em>
    <strong>40% OFF</strong>
    <p>Temporibus autem quibusdam et aut officiis debitis aut rerum necessitatibus saepe eveniet ut et voluptates repudiandae</p>
    <span class="ghost">SHOP NOW</span>
  </div>
  <div class="abs tile tile-meat" role="img" aria-label="Raw steaks and beef cuts with herbs on a dark stone board"><span>DUIS AUTE IRURE DOLOR REPREHENDERIT</span></div>
  <div class="abs tile tile-a" role="img" aria-label="Cows grazing in a green mountain valley"><span>EIUSMOD TEMPOR<br>INCIDIDUNT UT<br>LABORE</span></div>
  <div class="abs tile tile-b" role="img" aria-label="Cattle in a meadow below a mountain peak at sunset"><span>LOREM IPSUM DOLOR<br>SIT AMET,<br>CONSECTETUR</span></div>

  <h2 class="abs sec-title" style="top:1312px">OUR PRODUCTS</h2>
  <div class="abs arrow" style="left:39px;top:1510px;background:#c9c2bf"><svg width="8" height="10" viewBox="0 0 8 10"><path d="M6 1L2 5l4 4" stroke="#fff" stroke-width="2" fill="none"/></svg></div>
  <div class="abs arrow" style="left:1136px;top:1510px;background:var(--maroon)"><svg width="8" height="10" viewBox="0 0 8 10"><path d="M2 1l4 4-4 4" stroke="#fff" stroke-width="2" fill="none"/></svg></div>

  <div class="abs card" style="left:97px">
    <div class="img"><div role="img" aria-label="Packaged ground beef" style="background:linear-gradient(160deg,#e8a0a8,#c0303c 60%,#d8d8d8)"></div><span class="tag">SAVE 30%</span></div>
    <div class="name">Ground beef duis aute iru re dol reprehenderit</div>
    <div class="stars">★★★★★</div><div class="price">$39.00</div>
  </div>
  <div class="abs card" style="left:358px">
    <div class="img"><div role="img" aria-label="Beef steak in a sealed plastic tray" style="background:linear-gradient(160deg,#4a4a4a,#b8404a 45%,#3a3a3a)"></div><span class="tag">SAVE 30%</span></div>
    <div class="name">Beef tray excepteur sint occaecat cupida</div>
    <div class="stars">★★★★★</div><div class="price">$19.00</div>
  </div>
  <div class="abs card featured" style="left:618px">
    <div class="img" role="img" aria-label="Red beef cuts in vacuum packaging on display"></div>
    <div class="name">Meat in vacuum packaging lorem ipsum dolor</div>
    <div class="stars">★★★★★</div><div class="price">$55.00</div>
  </div>
  <div class="abs card" style="left:879px">
    <div class="img"><div role="img" aria-label="Row of beef sausages" style="background:linear-gradient(160deg,#f0a060,#d0602a 55%,#b8501e)"></div><span class="tag">SAVE 30%</span></div>
    <div class="name">Beef sausages excepteur sint occaecat</div>
    <div class="stars">★★★★★</div><div class="price">$42.00</div>
  </div>

  <div class="abs about-bg"></div>
  <h2 class="abs sec-title" style="top:1876px">ABOUT LARKIN RIDGE PROVISIONS CO</h2>
  <div class="abs about-copy">
    <p>Lorem ipsum dolor sit amet, consectetur adipiscing elit, sed do eiusmod tempor incididunt ut labore et dolore magna aliqua. Ut enim ad minim veniam, quis nostrud exercitation ullamco laboris nisi ut aliquip ex ea commodo consequat. Duis aute irure dolor in reprehenderit in voluptate velit esse cillum dolore eu fugiat nulla pariatur. Excepteur sint occaecat cupidatat non proident, sunt in culpa qui officia deserunt mollit anim id est laborum.</p>
    <p>Lorem ipsum dolor sit amet, consectetur adipiscing elit, sed do eiusmod tempor incididunt ut labore et dolore magna aliqua. Ut eninsequat. Duis aute irure dolor in reprehenderit in voluptate velit esse cillum dolore eu fugiat nulla pariatur.</p>
  </div>
  <div class="abs btn-green">READ MORE</div>
  <div class="abs range" role="img" aria-label="Hazy blue mountain range above a golden pasture with grazing cattle and a wooden fence"></div>

  <h2 class="abs sec-title" style="top:2882px">WHAT OUR CUSTOMER SAYS</h2>
  <div class="abs review" style="left:111px;top:2981px;width:311px;height:336px">
    <div class="stars">★★★★★</div>
    <p>Temporibus autem quibusdam et aut officiis debitis aut rerum neus saepe facere mus, onis voluptas eveniet ut et voluptates repudae sint et molestiae non lorem recusadae.</p>
    <div class="who" style="top:251px"><div class="avatar" role="img" aria-label="Customer portrait"></div><div><b>Owen Hadley</b><small>United States</small></div></div>
  </div>
  <div class="abs review plain" style="left:454px;top:3020px;width:309px;height:335px">
    <div class="stars">★★★★★</div>
    <p>Itaque earum rerum hic tenetur a sapiene delectus, ut aut reiciels volupatibus maiores alias conse uatur aut perferndis doloribus asperiores reiciendis voluptatbus repellat</p>
    <div class="who" style="top:251px"><div class="avatar" role="img" aria-label="Customer portrait"></div><div><b>Lena Vargas</b><small>United States</small></div></div>
  </div>
  <div class="abs review" style="left:794px;top:2981px;width:311px;height:337px">
    <div class="stars">★★★★★</div>
    <p>At vero eos et accusamus et iusto odio dignissimos ducimus qui blaiis praesentium voluptum deleniti atque corrupti quos dolores et quas occaecati cupie non provident</p>
    <div class="who" style="top:251px"><div class="avatar" role="img" aria-label="Customer portrait"></div><div><b>Marcus Bell</b><small>United States</small></div></div>
  </div>
  <div class="abs review" style="left:1142px;top:3023px;width:311px;height:340px">
    <div class="stars">★★★★★</div>
    <p>At vero eos et accusamus et iusto odio dignissimos ducimus qui blaiis praesentium voluptum deleniti atque corrupti quos dolores et quas occaecati cupie non provident</p>
    <div class="who" style="top:251px"><div class="avatar" role="img" aria-label="Customer portrait"></div><div><b>Marcus Bell</b><small>United States</small></div></div>
  </div>

  <footer class="abs footer">
    <div class="fcol fcontact" style="left:111px">
      <h5>CONTACT US</h5>
      <ul>
        <li><svg width="12" height="16" viewBox="0 0 12 16"><path d="M6 0a6 6 0 00-6 6c0 4 6 10 6 10s6-6 6-10a6 6 0 00-6-6z" fill="#fff"/><circle cx="6" cy="6" r="2" fill="var(--green-dark)"/></svg><span>Larkin Ridge Provisions Co<br>United States</span></li>
        <li><svg width="13" height="13" viewBox="0 0 13 13"><path d="M3 0l2 3-1.5 1.5a8 8 0 005 5L10 8l3 2-1 3C6 13 0 7 0 1z" fill="#fff"/></svg><span>+1 555 014 2290</span></li>
        <li><svg width="13" height="10" viewBox="0 0 13 10"><rect width="13" height="10" fill="#fff"/><path d="M0 0l6.5 5L13 0" stroke="var(--green-dark)" fill="none"/></svg><span>info@larkinridgeprovisions.com</span></li>
      </ul>
    </div>
    <div class="fcol" style="left:416px"><h5>QUICK LINKS</h5><ul><li>Home</li><li>About</li><li>Meat Box</li><li>Recipes</li><li>Contact Us</li></ul></div>
    <div class="fcol" style="left:661px"><h5>HELP CENTER</h5><ul><li>FAQ</li><li>Warrently</li><li>Privacy Policy</li><li>Support Center</li><li>Terms &amp; Conditions</li></ul></div>
    <div class="fbrand">Larkin Ridge<br>Provisions Co</div>
    <div class="copyright"><i></i><span>Copyrights@2024 Larkin Ridge Provisions Co .All Rights Reserved</span><i></i></div>
  </footer>

  <div class="abs subscribe">
    <h4>SUBSCRIBE FOR JOIN US</h4>
    <div class="field"><span>Enter Your Email</span><b>SUBSCRIBE</b></div>
  </div>

</div>
</body>
</html>
```